Sports Bar we serve burgers wings beer. www.copperlanetaphouse.com

Want to have 3 coupons 1 that is buy 1 dinner get half off a dinner. buy 1 get 1 free lunch, 1$ draft.

Sports Bar

```html
<!DOCTYPE html>
<html lang="en">
<head>
<meta charset="utf-8">
<title>Copper Lane Taphouse – Amazing Food, Drink &amp; Sports</title>
<link rel="stylesheet" href="https://fonts.googleapis.com/css2?family=Oswald:wght@500;600;700&family=Open+Sans:ital,wght@0,600;0,700;0,800;1,600;1,800&display=swap">
<style>
  :root {
    --stage: #5a4330;
    --ink: #222222;
    --black: #0b0b0b;
    --white: #ffffff;
    --yellow: #ffe600;
    --yellow-deep: #f2c500;
    --green: #0d6b35;
    --grey-text: #333333;
  }
  * { margin: 0; padding: 0; box-sizing: border-box; }
  html, body {
    width: 1200px; height: 907px; overflow: hidden;
    background: var(--stage);
  }
  .flyer {
    position: absolute; left: 50px; top: 60px;
    width: 1100px; height: 788px;
    background: var(--white);
    overflow: hidden;
    box-shadow: 0 8px 24px rgba(0,0,0,.35);
  }
  .photo { position: absolute; left: 0; width: 460px; }
  .photo--burger { top: 0; height: 295px;
    background: radial-gradient(ellipse at 55% 55%, #c9772f 0%, #7a3b1a 40%, #3a2418 75%, #2a1f1a 100%); }
  .photo--platter { top: 303px; height: 259px;
    background: radial-gradient(ellipse at 55% 55%, #e9dccb 0%, #6c8a45 45%, #f1f1f1 75%, #ffffff 100%); }
  .photo--beer { top: 572px; height: 216px;
    background: linear-gradient(90deg, #3b2a22 0%, #d99a2a 25%, #f4c24a 50%, #d99a2a 75%, #3b2a22 100%); }
  .divider { position: absolute; left: 0; width: 460px; height: 8px; background: var(--yellow); }
  .divider--1 { top: 295px; } .divider--2 { top: 562px; }

  .frame { position: absolute; left: 0; top: 0; }

  .headline {
    position: absolute; right: 44px; top: 22px;
    font-family: "Oswald", sans-serif; font-weight: 700;
    font-size: 126px; line-height: 1; color: var(--ink);
    letter-spacing: -1px;
  }
  .tagline {
    position: absolute; right: 40px; top: 170px;
    font-family: "Open Sans", sans-serif; font-weight: 800; font-style: italic;
    font-size: 54px; line-height: 1; color: var(--green); letter-spacing: -.5px;
  }
  .quote {
    position: absolute; right: 38px; top: 250px; text-align: right;
    font-family: "Open Sans", sans-serif; color: var(--grey-text);
  }
  .quote__text { font-style: italic; font-weight: 600; font-size: 18px; }
  .quote__mark { font-style: normal; font-weight: 800; font-size: 22px; color: var(--green); }
  .quote__name { font-weight: 700; font-size: 19px; margin-top: 6px; }

  .coupon {
    position: absolute; top: 348px; width: 184px; height: 184px;
    display: flex; flex-direction: column; align-items: center; justify-content: center;
    font-family: "Oswald", sans-serif; font-weight: 600; text-align: center; line-height: 1.08;
    text-transform: uppercase;
  }
  .coupon svg { position: absolute; left: 0; top: 0; }
  .coupon span { position: relative; }
  .coupon--dinner { left: 428px; }
  .coupon--lunch { left: 648px; }
  .coupon--draft { left: 870px; }
  .coupon__dark { color: var(--ink); }
  .coupon__green { color: var(--green); }
  .coupon--dinner .coupon__dark { font-size: 23px; }
  .coupon--dinner .coupon__green { font-size: 22px; }
  .coupon--lunch .coupon__dark { font-size: 30px; }
  .coupon--lunch .coupon__green { font-size: 30px; }
  .coupon--draft .coupon__dark { font-size: 34px; }
  .coupon--draft .coupon__green { font-size: 40px; }

  .brand {
    position: absolute; left: 452px; top: 615px; width: 190px;
    display: flex; flex-direction: column; align-items: center; gap: 10px;
    font-family: "Open Sans", sans-serif; font-weight: 800; font-size: 26px;
    line-height: 1.05; color: var(--yellow); text-align: center;
  }
  .brand__dot { width: 16px; height: 16px; border-radius: 50%; background: var(--yellow); }
  .social { position: absolute; top: 712px; width: 26px; height: 26px; border-radius: 50%; background: var(--white); }
  .social--a { left: 625px; } .social--b { left: 666px; }

  .contact {
    position: absolute; right: 30px; top: 604px;
    font-family: "Open Sans", sans-serif; font-weight: 600; font-size: 18.5px;
    color: var(--white); text-align: right; line-height: 24px;
  }
  .contact__row { display: flex; justify-content: flex-end; align-items: center; gap: 14px; }
  .contact__row + .contact__row { margin-top: 16px; }
  .contact__icon { width: 18px; height: 18px; flex: none; }
</style>
</head>
<body>
  <main class="flyer">
    <div class="photo photo--burger" role="img" aria-label="Photo of a cheeseburger with lettuce, tomato, onion and pickles on a sesame bun"></div>
    <div class="divider divider--1"></div>
    <div class="photo photo--platter" role="img" aria-label="Photo of a platter of finger sandwiches with lemon and cucumber garnish"></div>
    <div class="divider divider--2"></div>
    <div class="photo photo--beer" role="img" aria-label="Photo of two frosty mugs of draft beer"></div>

    <svg class="frame" width="1100" height="788" viewBox="0 0 1100 788" aria-hidden="true">
      <path d="M478 0 C430 150 408 380 404 575" fill="none" stroke="var(--yellow)" stroke-width="7"/>
      <path d="M494 0 L548 0 C476 150 446 380 436 575 L412 575 C418 380 442 160 494 0 Z" fill="var(--black)"/>
      <path d="M548 0 L1100 0 L1100 575 L436 575 C446 380 476 150 548 0 Z" fill="var(--white)"/>
      <path d="M412 582 L1100 582 L1100 788 L462 788 C440 720 420 650 412 582 Z" fill="var(--black)"/>
      <rect x="412" y="572" width="688" height="10" fill="var(--yellow)"/>
    </svg>

    <h1 class="headline">Amazing</h1>
    <p class="tagline">Food, Drink &amp; Sports</p>
    <blockquote class="quote">
      <p class="quote__text"><span class="quote__mark">“</span> Copper Lane Taphouse is the only way I travel. I use it every time! <span class="quote__mark">”</span></p>
      <p class="quote__name">Dana Whitlock</p>
    </blockquote>

    <div class="coupon coupon--dinner">
      <svg width="184" height="184" viewBox="0 0 184 184" aria-hidden="true">
        <circle cx="92" cy="92" r="90" fill="var(--white)"/>
        <circle cx="92" cy="92" r="88" fill="none" stroke="var(--green)" stroke-width="2" stroke-dasharray="5 4"/>
        <circle cx="92" cy="92" r="78" fill="var(--yellow)" stroke="var(--black)" stroke-width="5"/>
      </svg>
      <span class="coupon__dark">Buy 1 Dinner</span>
      <span class="coupon__green">Get Half<br>Off a Dinner</span>
    </div>
    <div class="coupon coupon--lunch">
      <svg width="184" height="184" viewBox="0 0 184 184" aria-hidden="true">
        <circle cx="92" cy="92" r="90" fill="var(--white)"/>
        <circle cx="92" cy="92" r="88" fill="none" stroke="var(--green)" stroke-width="2" stroke-dasharray="5 4"/>
        <circle cx="92" cy="92" r="78" fill="var(--yellow)" stroke="var(--black)" stroke-width="5"/>
      </svg>
      <span class="coupon__dark">Buy 1</span>
      <span class="coupon__green">Get 1 Free<br>Lunch</span>
    </div>
    <div class="coupon coupon--draft">
      <svg width="184" height="184" viewBox="0 0 184 184" aria-hidden="true">
        <circle cx="92" cy="92" r="90" fill="var(--white)"/>
        <circle cx="92" cy="92" r="88" fill="none" stroke="var(--green)" stroke-width="2" stroke-dasharray="5 4"/>
        <circle cx="92" cy="92" r="78" fill="var(--yellow)" stroke="var(--black)" stroke-width="5"/>
      </svg>
      <span class="coupon__dark">1$</span>
      <span class="coupon__green">Draft</span>
    </div>

    <div class="brand">
      <span>Copper Lane<br>Taphouse</span>
      <span class="brand__dot"></span>
    </div>
    <span class="social social--a"></span>
    <span class="social social--b"></span>

    <address class="contact">
      <div class="contact__row">
        <span>+1.480.555.0187</span>
        <svg class="contact__icon" viewBox="0 0 24 24" aria-hidden="true"><path d="M6.6 10.8a15 15 0 0 0 6.6 6.6l2.2-2.2a1 1 0 0 1 1-.25 11 11 0 0 0 3.6.6 1 1 0 0 1 1 1V20a1 1 0 0 1-1 1A17 17 0 0 1 3 4a1 1 0 0 1 1-1h3.5a1 1 0 0 1 1 1 11 11 0 0 0 .6 3.6 1 1 0 0 1-.25 1z" fill="var(--yellow)"/></svg>
      </div>
      <div class="contact__row">
        <span>1480 West Ridge Road<br>Mesa Vista AZ 85299 us</span>
        <svg class="contact__icon" viewBox="0 0 24 24" aria-hidden="true"><path d="M12 3 2 12h3v8h5v-5h4v5h5v-8h3z" fill="var(--yellow)"/></svg>
      </div>
      <div class="contact__row">
        <span>www.copperlanetaphouse.com</span>
        <svg class="contact__icon" viewBox="0 0 24 24" aria-hidden="true"><circle cx="12" cy="12" r="10" fill="var(--yellow)"/><path d="M2 12h20M12 2c3 3 3 17 0 20M12 2c-3 3-3 17 0 20M4 7h16M4 17h16" fill="none" stroke="var(--black)" stroke-width="1.3"/></svg>
      </div>
    </address>
  </main>
</body>
</html>
```